Business Card Design for Logistics Startup

Link to my logo source file -
https://www.fylvault.com/sh/qormx7pl2vkc8wd/KLmrT9_ZPq4BnWvHhYtaeCxo?dl=0

We want a statement in our business card!
I have go thru your portfolio, and invites 3 of you guys to design my business card as the previous designer cannot give me the feel.
Let me know if you want any information.
Thanks.
Updates

Target Market(s)

Transport and Logistics
: Shippers, Freight Forwarders and Carriers.

Industry/Entity Type

Business

Contact Information for Business Card

Our details;

Name: Marcus Loh
Designation: General Manager
Mobile: +65 91234508
Email: marcus.loh@corvinmarl.com
Address: 7 Lorong Pelita Rise
RHOMB Tower #09-17
Singapore 639217

Name: Victor Yeo
Designation: Director
Mobile: +65 93416672
Email: victor.yeo@corvinmarl.com
RHOMB Tower #09-17
Singapore 639217

Colors
f37122

Requirements
Must have
• Logo from my source file.
• Please included tagline: Transport and Logistics
• If you guy can think of a tagline - Using E and S, that will be perfect. Such as Excellence in Service..

```html
<!DOCTYPE html>
<html lang="en">
<head>
<meta charset="utf-8">
<title>Corvin Marl Business Card</title>
<link href="https://fonts.googleapis.com/css2?family=Open+Sans:wght@400;600&display=swap" rel="stylesheet">
<style>
  :root {
    --brand-orange: #f37122;
    --card-white: #ffffff;
    --ink-grey: #6b6b6b;
    --rule-grey: #cfcfcf;
    --backdrop: #ece9e5;
  }
  html, body {
    margin: 0;
    padding: 0;
    width: 1200px;
    height: 1000px;
    overflow: hidden;
    background: var(--backdrop);
    font-family: "Open Sans", Arial, sans-serif;
  }
  .canvas {
    position: relative;
    width: 1200px;
    height: 1000px;
  }
  .card {
    position: absolute;
    left: 266px;
    width: 666px;
    height: 396px;
    overflow: hidden;
    box-shadow: 0 4px 14px rgba(0,0,0,0.18);
  }
  .card--front { top: 74px; background: var(--card-white); }
  .card--back { top: 534px; background: var(--brand-orange); }

  .brand {
    position: absolute;
    display: flex;
    align-items: center;
    font-weight: 600;
    letter-spacing: 4px;
    line-height: 1;
    white-space: nowrap;
  }
  .card--front .brand { left: 33px; top: 49px; gap: 24px; color: var(--brand-orange); font-size: 29px; }
  .card--front .brand__mark { width: 90px; height: 90px; background: var(--brand-orange); }
  .card--back .brand { left: 90px; top: 128px; gap: 36px; color: var(--card-white); font-size: 35px; }
  .card--back .brand__mark { width: 120px; height: 120px; background: var(--card-white); }

  .holder { position: absolute; left: 33px; top: 190px; }
  .holder__name { margin: 0; color: var(--brand-orange); font-size: 24px; font-weight: 600; line-height: 1.2; }
  .holder__role { margin: 0; color: var(--ink-grey); font-size: 16px; line-height: 1.4; }

  .rule { position: absolute; left: 33px; top: 255px; width: 600px; height: 1px; background: var(--rule-grey); }

  .contact { position: absolute; left: 33px; top: 282px; color: var(--ink-grey); font-size: 16px; }
  .contact__row { display: flex; align-items: center; gap: 9px; height: 28px; }
  .contact__icon { width: 15px; height: 15px; fill: var(--brand-orange); }

  .address {
    position: absolute; right: 33px; top: 279px; margin: 0;
    color: var(--ink-grey); font-size: 16px; line-height: 24.5px;
    text-align: right; font-style: normal;
  }

  .footer-bar { position: absolute; left: 0; bottom: 0; width: 666px; height: 22px; background: var(--brand-orange); }
  .footer-bar__gap { position: absolute; left: 450px; top: 0; width: 5px; height: 22px; background: var(--card-white); }

  .tagline {
    position: absolute; left: 0; right: 0; top: 346px; margin: 0;
    text-align: center; color: var(--card-white);
    font-size: 16px; letter-spacing: 1.6px;
  }
</style>
</head>
<body>
<main class="canvas">
  <section class="card card--front" aria-label="Business card front">
    <div class="brand"><span class="brand__mark"></span><span class="brand__name">CORVIN MARL</span></div>
    <div class="holder">
      <h1 class="holder__name">MARCUS LOH</h1>
      <p class="holder__role">General Manager</p>
    </div>
    <div class="rule"></div>
    <div class="contact">
      <div class="contact__row">
        <svg class="contact__icon" viewBox="0 0 16 16" aria-hidden="true"><path d="M3 3c2-2 10-2 12 0l-1 3-3-1V4H5v1L2 6z"/><path d="M4 8h8l2 5H2z"/><circle cx="8" cy="10.5" r="1.3" fill="#fff"/></svg>
        <span>+65 91234508</span>
      </div>
      <div class="contact__row">
        <svg class="contact__icon" viewBox="0 0 16 16" aria-hidden="true"><path d="M1 4h14v1L8 9 1 5z"/><path d="M1 6.5l7 4 7-4V13H1z"/></svg>
        <span>marcus.loh@corvinmarl.com</span>
      </div>
    </div>
    <address class="address">7 Lorong Pelita Rise<br>RHOMB Tower #09-17<br>Singapore 639217</address>
    <div class="footer-bar"><span class="footer-bar__gap"></span></div>
  </section>

  <section class="card card--back" aria-label="Business card back">
    <div class="brand"><span class="brand__mark"></span><span class="brand__name">CORVIN MARL</span></div>
    <p class="tagline">Transport and Logistics | Service Assured</p>
  </section>
</main>
</body>
</html>
```